Powerpoint design for Summit Lane Advisors

We would like to have a Power point template/design with flexibilities and good opportunities to do changes.
• Be able to change in image background
• Themes are SLA colors and complementary colors. Please come with suggestions.
• Alternate white and blue background
• Standard functions and opportunities within Powerpoint should be able to be used or be accessible.
• Feel free to change/alter the logo for example remove or separate the text in the logo ("Summit Lane Advisors" ) and the tagline ("we create competitiveness")
• www.summitlaneadvisors.se

```html
<!DOCTYPE html>
<html lang="en">
<head>
<meta charset="utf-8">
<title>Summit Lane Advisors – Presentation Template</title>
<link rel="stylesheet" href="https://fonts.googleapis.com/css2?family=Roboto:wght@400;500;700;900&family=Open+Sans:wght@400;600&display=swap">
<style>
  :root {
    --navy: #0c2c5e;
    --navy-deep: #0a2654;
    --brand-blue: #123f85;
    --ink: #333a44;
    --white: #ffffff;
    --page: #e3e4e6;
    --teal: #3fb6d0;
  }
  * { box-sizing: border-box; margin: 0; padding: 0; }
  html, body { width: 1200px; height: 4095px; overflow: hidden; }
  body { background: var(--page); position: relative; font-family: "Open Sans", Arial, sans-serif; color: var(--ink); }

  .slide { position: absolute; left: 113px; width: 960px; height: 720px; overflow: hidden; }
  .slide--light { background: var(--white); }
  .slide--dark { background: var(--navy); color: var(--white); }

  .brand-mark { position: absolute; left: 22px; top: 28px; display: flex; align-items: center; gap: 8px;
    font-family: "Roboto", Arial, sans-serif; font-weight: 900; font-size: 44px; letter-spacing: 1px; color: var(--navy); }
  .brand-mark .dot { width: 12px; height: 12px; border-radius: 50%; background: currentColor; }
  .slide--dark .brand-mark { color: var(--white); }

  .brand-name { position: absolute; right: 22px; top: 16px; text-align: center; font-family: "Roboto", Arial, sans-serif; color: var(--brand-blue); }
  .brand-name .name { font-size: 32px; font-weight: 400; line-height: 1.1; }
  .brand-name .tagline { font-size: 16px; letter-spacing: 3px; font-weight: 500; }
  .slide--dark .brand-name { color: var(--white); }

  .footer-rule { position: absolute; left: 0; right: 0; bottom: 0; height: 20px; }
  .footer-rule::before { content: ""; position: absolute; left: 0; right: 0; top: 0; height: 11px; background: var(--navy); }
  .footer-rule::after { content: ""; position: absolute; left: 0; right: 0; bottom: 0; height: 5px; background: var(--navy); }
  .slide--dark .footer-rule { background: var(--white); height: 22px; }
  .slide--dark .footer-rule::before { top: 0; height: 14px; }
  .slide--dark .footer-rule::after { height: 5px; }

  .photo { position: absolute; }

  h2 { font-family: "Roboto", Arial, sans-serif; font-weight: 700; color: var(--navy); }

  /* Slide 1 */
  .intro-title { position: absolute; left: 48px; top: 157px; width: 400px; font-size: 30px; line-height: 1.2; text-transform: uppercase; }
  .intro-body { position: absolute; left: 51px; top: 290px; width: 405px; font-size: 18.5px; line-height: 25px; }

  /* Slide 2 */
  .statement-frame { position: absolute; left: 126px; top: 186px; width: 709px; height: 332px; border: 2px solid var(--white); }
  .statement-frame h2 { position: absolute; top: -22px; left: 50%; transform: translateX(-50%); white-space: nowrap;
    padding: 0 14px; background: var(--navy-deep); color: var(--white); font-size: 31px; letter-spacing: .3px; }
  .statement-frame p { position: absolute; left: 60px; right: 60px; top: 68px; text-align: center; font-size: 19.5px; line-height: 28px; }

  /* Slide 3 */
  .focus-title { position: absolute; left: 0; right: 0; top: 124px; text-align: center; font-size: 30px; }
  .focus-col { position: absolute; top: 203px; width: 436px; }
  .focus-col .photo { position: static; display: block; width: 436px; height: 226px; }
  .focus-col h3 { margin-top: 40px; font-family: "Roboto", Arial, sans-serif; font-weight: 700; font-size: 17.5px; line-height: 22px; color: var(--brand-blue); text-transform: uppercase; }
  .focus-list { list-style: none; margin-top: 14px; }
  .focus-list li { position: relative; padding-left: 17px; font-size: 15.5px; line-height: 32px; color: #222; }
  .focus-list li::before { content: ""; position: absolute; left: 3px; top: 11px; border-left: 6px solid #222; border-top: 5px solid transparent; border-bottom: 5px solid transparent; }

  /* Slide 4 */
  .pillar { position: absolute; width: 418px; height: 203px; border: 1.5px solid rgba(255,255,255,.85); }
  .pillar h3 { position: absolute; top: -16px; left: 42px; padding: 0 12px; background: var(--navy);
    font-family: "Roboto", Arial, sans-serif; font-weight: 500; font-size: 23px; line-height: 30px; color: var(--white); white-space: nowrap; }
  .pillar p { position: absolute; left: 37px; right: 30px; top: 35px; font-size: 16.5px; line-height: 25px; }

  /* Slide 5 */
  .feature-title { position: absolute; left: 556px; top: 166px; width: 360px; font-size: 30px; line-height: 36px; color: var(--brand-blue); font-weight: 700; }
  .feature-body { position: absolute; left: 559px; top: 256px; width: 370px; font-size: 15.5px; line-height: 20px; color: #111; }
  .feature-body p + p { margin-top: 20px; }
</style>
</head>
<body>

<!-- Slide 1: Passion -->
<section class="slide slide--light" style="top:103px">
  <div class="brand-mark"><span class="dot"></span>SLA</div>
  <div class="brand-name"><div class="name">Summit Lane Advisors</div><div class="tagline">We create competitiveness</div></div>
  <h2 class="intro-title">Our passion is the key factor for customer success</h2>
  <p class="intro-body">Sed ut perspiciatis unde omnis iste natus error sit voluptatem accusantium doloremque lauda ntium, totam rem aperiam, eaque ipsa quae ab illo inventore veritatis et quasi architecto beat ae vitae dicta sunt explicabo. Nemo enim ipsam voluptatem quia voluptas sit aspernatur aut odit aut fugit, sed quia consequuntur magni dolores eos qui ratione voluptatem sequi nesciunt. Neque porro quisquam est, qui dolorem ipsum quia dolor sit amet, consectetur, adipisci velit, sed quia non numquam eius modi tempora incidunt ut labore et dolore magnam aliquam.</p>
  <div class="photo" role="img" aria-label="Business person in a suit pointing at a glowing digital growth chart"
       style="left:485px;top:124px;width:475px;height:532px;background:radial-gradient(circle at 62% 60%,#3aa7c6 0%,#1c4f7e 30%,#122b4e 65%,#0b1a33 100%)"></div>
  <div class="footer-rule"></div>
</section>

<!-- Slide 2: Statement -->
<section class="slide slide--dark" style="top:887px">
  <div class="photo" role="img" aria-label="Deep blue background with a glowing wave of teal particles"
       style="inset:0;background:radial-gradient(ellipse 80% 30% at 55% 80%,#1f7fa6 0%,rgba(18,60,110,.6) 45%,transparent 75%),linear-gradient(180deg,#0a2654 0%,#0c2c5e 55%,#0a2a58 100%)"></div>
  <div class="brand-mark"><span class="dot"></span>SLA</div>
  <div class="brand-name"><div class="name">Summit Lane Advisors</div><div class="tagline">We create competitiveness</div></div>
  <div class="statement-frame">
    <h2>WE CREATE DIGITAL COMPETITIVENESS</h2>
    <p>There are many variations of passages of Lorem Ipsum available, but the majority have suffered alteration in some form, by injected humour, or randomised words which don't look even slightly believable. If you are going to use a passage of Lorem Ipsum, you need to be sure there isn't anything embarrassing hidden in the middle of text. All the Lorem Ipsum generators on the Internet tend to repeat predefined chunks a</p>
  </div>
  <div class="footer-rule"></div>
</section>

<!-- Slide 3: Focus areas -->
<section class="slide slide--light" style="top:1674px">
  <div class="brand-mark"><span class="dot"></span>SLA</div>
  <div class="brand-name"><div class="name">Summit Lane Advisors</div><div class="tagline">We create competitiveness</div></div>
  <h2 class="focus-title">FOCUS AREAS</h2>
  <div class="focus-col" style="left:27px">
    <div class="photo" role="img" aria-label="Hands above a tablet with glowing app icons floating upward"
         style="background:radial-gradient(circle at 48% 72%,#f3c27a 0%,#a0612f 14%,#3a2a24 34%,#141416 70%)"></div>
    <h3>We work with the following in<br>digital development</h3>
    <ul class="focus-list">
      <li>Customer and user experience</li>
      <li>Systems and solutions in store</li>
      <li>Digital development&nbsp; and transformation</li>
      <li>Digitalization and technology</li>
    </ul>
  </div>
  <div class="focus-col" style="left:500px">
    <div class="photo" role="img" aria-label="Black and white overhead view of a café with tables and chairs"
         style="background:linear-gradient(135deg,#9a9a9a 0%,#6e6e6e 40%,#4a4a4a 70%,#2a2a2a 100%)"></div>
    <h3>We work with the following<br>technologies</h3>
    <ul class="focus-list">
      <li>Digital Signage</li>
      <li>Sound solutions</li>
      <li>Queue management solutions</li>
      <li>People counter technology</li>
    </ul>
  </div>
  <div class="footer-rule"></div>
</section>

<!-- Slide 4: Approach -->
<section class="slide slide--dark" style="top:2462px">
  <div class="brand-mark"><span class="dot"></span>SLA</div>
  <div class="brand-name"><div class="name">Summit Lane Advisors</div><div class="tagline">We create competitiveness</div></div>
  <div class="pillar" style="left:38px;top:181px">
    <h3>Our passion</h3>
    <p>Summit Lane Advisors´s passion is to understand and follow the digital transformation and development and to use this knowledge to help customers to gain competitiveness.</p>
  </div>
  <div class="pillar" style="left:500px;top:181px">
    <h3>Concept Implementation</h3>
    <p>New concepts and solutions are very dependent on a good implementation plan to be successful. Together with the customer we work out the best set-up.</p>
  </div>
  <div class="pillar" style="left:38px;top:437px">
    <h3>Concept Development</h3>
    <p>Together with our customers we identify the business opportunities and challenges and develop concepts according to this. The concepts include proposed digital solutions and best praxis.</p>
  </div>
  <div class="pillar" style="left:500px;top:437px">
    <h3>Analytics and evaluation</h3>
    <p>Before, during and after concept development it is crucial to regularly do analytics and evaluation. The result of this will be used to improve and refine concept development and concept implementation.</p>
  </div>
  <div class="footer-rule"></div>
</section>

<!-- Slide 5: Digital development -->
<section class="slide slide--light" style="top:3238px">
  <div class="brand-mark"><span class="dot"></span>SLA</div>
  <div class="brand-name"><div class="name">Summit Lane Advisors</div><div class="tagline">We create competitiveness</div></div>
  <div class="photo" role="img" aria-label="Hands typing on a laptop overlaid with blue program code"
       style="left:27px;top:127px;width:490px;height:537px;background:linear-gradient(120deg,#1a3f8a 0%,#3f6bb8 35%,#c8d6ee 60%,#2b58a8 80%,#0e2a6a 100%)"></div>
  <h2 class="feature-title">Digital development and transformation</h2>
  <div class="feature-body">
    <p>Digital transformation is changing the way we live, what we do and how we communicate with each other as well as how we do our business and shopping.</p>
    <p>The customers are better informed and more independent in their decisions. The digital transformation has created great possibilities in more channels than ever.</p>
    <p>To get knowledge about how products, services and information can be consumed with digital concepts and solutions is more necessary than ever for companies. They need this to adapt to their customers wishes and requirements. It is essential to go from believing to knowing to implementing.&nbsp; Using the knowledge about digital development and concepts give companies the right background to invest in digital solutions.</p>
  </div>
  <div class="footer-rule"></div>
</section>

</body>
</html>
```